Sun-Pod Coffee Kiosks Webdesign project

Sun-Pod Coffee Kiosks provides coffee carts, kiosks, and/or drive thrus depending on location. At Sun-Pod our company focuses on offering healthy snack & drink options for people on the go as well as nutritional coaching with our daily "Pod notes." We will provide some healthy snacks as well.

We offer all organic coffee & espresso drinks,100% real fruit & vegetable smoothies, protein shakes, and healthy breakfast/snack items.

I want "balance" to be a big theme in the website design. True well-being is a balance of body (health), mind (emotional well-being) and spirit (we are a Christian based company who loves and accepts all people, sexual orientation, religions, ect)

My parents are missionaries and founded the Nicaraguan organization "Bright Path Outreach Nicaragua" over 11 years ago ( www.brightpathoutreach.org ). Sun-Pod plans to be a financial partner to their mission so 10% of profits or 2% of total revenue, whichever is greater will go to Bright Path and their church plants & medical/dental clinic. I want this and info about Bright Path to have a page on the website.

Target Market(s)

Ages 18-54 (target coffee customer).

Industry/Entity Type

Financial

Requirements
Must have
• -Home page
-Menu page
-Locations page/contact page
-Kiosk options page (cart, kiosk & drive thru descriptions, pics, traffic & location needs, ect)
-Fundraising/Bright Path Outreach Nicaragua page
Nice to have
• I have a logo designed that I attached. I would like the colors to be dark brown, light brown, and a lime green. My business card is also attached.

```html
<!DOCTYPE html>
<html lang="en">
<head>
<meta charset="utf-8">
<title>Sun-Pod Organic Coffee</title>
<link href="https://fonts.googleapis.com/css2?family=Roboto+Condensed:wght@300;400;700&family=PT+Sans:wght@400;700&family=Crimson+Text:ital@0;1&display=swap" rel="stylesheet">
<style>
:root{
  --brown:#6e3b28;
  --brown-dark:#3b2116;
  --brown-light:#b07a4f;
  --lime:#7aaa12;
  --white:#ffffff;
  --text:#555555;
  --nav:#6a6a6a;
}
*{margin:0;padding:0;box-sizing:border-box}
html,body{width:1157px;height:1200px;overflow:hidden;background:var(--white)}
body{position:relative;font-family:"PT Sans",sans-serif;color:var(--text)}
.abs{position:absolute}

/* header */
.site-header{left:0;top:0;width:1157px;height:105px;background:var(--white)}
.brand{left:174px;top:30px;width:150px;text-align:center}
.brand-name{font-family:"Roboto Condensed",sans-serif;font-size:36px;font-weight:400;color:var(--brown-dark);line-height:1}
.brand-sub{font-size:8px;letter-spacing:2px;color:var(--brown);font-weight:700;margin-top:4px}
.nav a{position:absolute;top:52px;font-size:11px;color:var(--nav);text-decoration:none;text-transform:uppercase}
.nav .active{top:0;left:332px;width:109px;height:105px;background:var(--brown);color:var(--white);line-height:117px;text-align:center}

/* hero */
.hero{left:0;top:105px;width:1157px;height:502px;background:linear-gradient(100deg,#6b3a1e 0%,#a86a3a 30%,#c99468 55%,#b57a4e 75%,#8a5530 100%)}
.hero-mark{left:806px;top:40px;width:74px;height:74px;border-radius:50%;background:var(--white)}
.hero-title{right:180px;top:122px;font-family:"Roboto Condensed",sans-serif;font-size:66px;color:var(--white);line-height:1;font-weight:400}
.hero-tagline{right:175px;top:206px;width:460px;text-align:right;font-size:12.3px;font-weight:700;color:var(--white);line-height:20.6px;text-transform:uppercase}
.slide-arrow{top:225px;width:46px;height:47px;background:rgba(60,30,15,.55)}
.slide-arrow svg{position:absolute;left:15px;top:14px}

/* intro cards */
.intro{top:494px;width:395px;height:170px;background:var(--white)}
.intro-photo{left:22px;top:22px;width:146px;height:146px;border-radius:50%}
.intro-ring{left:28px;top:24px;width:146px;height:146px;border-radius:50%;border:3px solid var(--brown)}
.intro-kicker{left:200px;top:20px;font-family:"Roboto Condensed",sans-serif;font-size:24px;color:var(--lime)}
.intro-title{left:200px;top:47px;font-family:"Roboto Condensed",sans-serif;font-size:42px;color:var(--brown);line-height:1.1}
.intro-text{left:205px;top:100px;width:165px;font-size:8.6px;line-height:15px;color:var(--text)}

/* offers */
.offer-kicker{left:172px;top:684px;font-family:"Roboto Condensed",sans-serif;font-weight:300;font-size:34px;color:var(--lime)}
.offer-title{left:173px;top:720px;font-family:"Roboto Condensed",sans-serif;font-weight:400;font-size:25px;color:var(--brown)}
.mini-arrow{top:725px;width:17px;height:16px;background:var(--brown-dark)}
.mini-arrow svg{position:absolute;left:5px;top:4px}
.offer-card{top:764px;width:260px}
.offer-head{height:32px;background:var(--lime);color:var(--white);font-size:11px;line-height:32px;padding-left:17px;text-transform:uppercase}
.offer-photo{height:127px}
.offer-text{margin-top:17px;font-size:8.6px;line-height:15px;color:var(--text)}
.btn{display:inline-block;margin-top:12px;width:89px;height:23px;line-height:23px;text-align:center;background:var(--brown);color:var(--white);font-size:10px;text-transform:uppercase}

/* testimonials */
.feeds{left:731px;top:693px;width:252px;height:338px;background:var(--brown)}
.feeds-kicker{left:23px;top:17px;font-family:"Roboto Condensed",sans-serif;font-size:22px;color:var(--white)}
.feeds-title{left:23px;top:44px;font-family:"Roboto Condensed",sans-serif;font-size:38px;color:var(--white);font-weight:400}
.feeds .mini-arrow{top:20px;background:rgba(0,0,0,.35)}
.quote-mark{font-family:"Crimson Text",serif;font-size:38px;color:var(--white);line-height:1}
.quote-head{left:50px;top:110px;font-size:8.6px;font-weight:700;color:var(--white);text-transform:uppercase}
.quote-photo{left:26px;top:128px;width:90px;height:90px;border-radius:50%;border:2px solid var(--lime)}
.quote-text{left:132px;top:133px;width:110px;font-size:8.6px;line-height:15px;color:var(--white)}
.quote-name{left:27px;top:237px;font-family:"Crimson Text",serif;font-size:12px;letter-spacing:.5px;color:var(--white);text-transform:uppercase}
.quote-date{left:27px;top:257px;font-family:"Crimson Text",serif;font-size:9.5px;color:var(--white);text-transform:uppercase}
.feeds-more{left:0;top:289px;width:252px;height:49px;background:var(--lime);color:var(--white);font-family:"Roboto Condensed",sans-serif;font-size:31px;line-height:49px;text-align:center}

/* footer */
.site-footer{left:0;top:1073px;width:1157px;height:127px;background:var(--brown)}
.pledge{left:0;top:14px;width:1157px;text-align:center;font-family:"Crimson Text",serif;font-style:italic;font-size:22px;color:var(--white)}
.footer-rule{left:174px;top:53px;width:809px;height:1px;background:rgba(255,255,255,.25)}
.footer-nav{left:178px;top:70px;font-size:8.8px;color:var(--white);text-transform:uppercase;word-spacing:1px}
.footer-nav span{margin:0 9px}
.copyright{left:178px;top:96px;font-size:8.6px;color:var(--white);text-transform:uppercase}
.follow{left:807px;top:85px;font-size:8.6px;font-weight:700;color:var(--white);text-transform:uppercase}
.social{top:77px;width:26px;height:26px;border-radius:50%}
</style>
</head>
<body>

<header class="site-header abs">
  <div class="brand abs">
    <div class="brand-name">Sun-Pod</div>
    <div class="brand-sub">ORGANIC COFFEE</div>
  </div>
  <nav class="nav">
    <a class="active" href="#">About Us</a>
    <a href="#" style="left:460px">Menu</a>
    <a href="#" style="left:540px">Locations</a>
    <a href="#" style="left:645px">Kiosk Options</a>
    <a href="#" style="left:770px">Fundraising</a>
    <a href="#" style="left:888px">Contact Us</a>
  </nav>
</header>

<section class="hero abs" role="img" aria-label="Coffee grinder, burlap sack of roasted beans and a white cup of coffee on a warm brown backdrop">
  <div class="hero-mark abs"></div>
  <div class="hero-title abs">Sun-Pod</div>
  <p class="hero-tagline abs">We provide coffee carts, kiosks, and/or drive thrus depending on<br>locations, we offer all organic coffee &amp; espresso drinks,100%<br>real fruit &amp; vegetable smoothies, protein shakes, and healthy<br>breakfast/snack items</p>
  <div class="slide-arrow abs" style="left:107px"><svg width="14" height="20"><path d="M12 1 L2 10 L12 19" fill="none" stroke="#fff" stroke-width="1.5"/></svg></div>
  <div class="slide-arrow abs" style="left:1016px"><svg width="14" height="20"><path d="M2 1 L12 10 L2 19" fill="none" stroke="#fff" stroke-width="1.5"/></svg></div>
</section>

<article class="intro abs" style="left:174px">
  <div class="intro-ring abs"></div>
  <div class="intro-photo abs" role="img" aria-label="Cup of coffee with beans on a saucer" style="background:radial-gradient(circle at 45% 40%,#d8a070,#8a4a22 55%,#4a2212)"></div>
  <div class="intro-kicker abs">Welcome to</div>
  <div class="intro-title abs">Sun Pod</div>
  <p class="intro-text abs">embarrassing hidden in the middle of text. All the Lorem Ipsum generators on the Internet tend to repeat predefined chunks as necessary.</p>
</article>

<article class="intro abs" style="left:588px">
  <div class="intro-ring abs"></div>
  <div class="intro-photo abs" role="img" aria-label="Fresh fruit smoothies with kiwi and orange slices" style="background:radial-gradient(circle at 55% 50%,#c8d860,#e0a030 45%,#b0301a 85%)"></div>
  <div class="intro-kicker abs">About</div>
  <div class="intro-title abs">Sun Pod</div>
  <p class="intro-text abs">embarrassing hidden in the middle of text. All the Lorem Ipsum generators on the Internet tend to repeat predefined chunks as necessary.</p>
</article>

<h2 class="offer-kicker abs">WE OFFER ALL</h2>
<h3 class="offer-title abs">ORGANIC COFFEE &amp; ESPRESSO DRINKS</h3>
<div class="mini-arrow abs" style="left:674px"><svg width="7" height="8"><path d="M6 0 L1 4 L6 8" fill="none" stroke="#fff"/></svg></div>
<div class="mini-arrow abs" style="left:694px"><svg width="7" height="8"><path d="M1 0 L6 4 L1 8" fill="none" stroke="#fff"/></svg></div>

<article class="offer-card abs" style="left:174px">
  <div class="offer-head">Vegetable Smoothies</div>
  <div class="offer-photo" role="img" aria-label="Glasses of vegetable and fruit smoothies" style="background:linear-gradient(90deg,#e8c9a8,#c98a5a 35%,#a8b848 65%,#6a8a20)"></div>
  <p class="offer-text">Embarrassing hidden in the middle of text. All the Lorem Ipsum generators on the Internet tend to repeat predefined chunks as embarrassing hidden in the middle of text. All the Lorem Ipsum generators on the Internet tend to repeat...</p>
  <a class="btn">Read More</a>
</article>

<article class="offer-card abs" style="left:452px">
  <div class="offer-head">Organic Coffee &amp; Espresso Drinks</div>
  <div class="offer-photo" role="img" aria-label="Cup of espresso with sugar cubes and a spoon" style="background:linear-gradient(135deg,#4a3020,#8a6a50 40%,#e8e0d8 70%,#c8b8a8)"></div>
  <p class="offer-text">Embarrassing hidden in the middle of text. All the Lorem Ipsum generators on the Internet tend to repeat predefined chunks as embarrassing hidden in the middle of text. All the Lorem Ipsum generators on the Internet tend to repeat...</p>
  <a class="btn">Read More</a>
</article>

<aside class="feeds abs">
  <div class="feeds-kicker abs">HAPPY</div>
  <div class="feeds-title abs">CUSTOMERS</div>
  <div class="mini-arrow abs" style="left:202px"><svg width="7" height="8"><path d="M6 0 L1 4 L6 8" fill="none" stroke="#fff"/></svg></div>
  <div class="mini-arrow abs" style="left:222px"><svg width="7" height="8"><path d="M1 0 L6 4 L1 8" fill="none" stroke="#fff"/></svg></div>
  <div class="quote-mark abs" style="left:18px;top:96px">&ldquo;</div>
  <div class="quote-head abs">Embarrassing hidden in the middle</div>
  <div class="quote-photo abs" role="img" aria-label="Fruit smoothies with kiwi and orange" style="background:radial-gradient(circle at 55% 50%,#c8d860,#e0a030 45%,#b0301a 85%)"></div>
  <p class="quote-text abs">Embarrassing hidden in the middle of text. All the Lorem Ipsum generators on the Internet tend to repeat predefined...</p>
  <div class="quote-mark abs" style="left:212px;top:210px">&rdquo;</div>
  <div class="quote-name abs">Lena Marsh</div>
  <div class="quote-date abs">20 Jul 2013</div>
  <div class="feeds-more abs">VIEW MORE FEEDS</div>
</aside>

<footer class="site-footer abs">
  <p class="pledge abs">10% of all profits will be sent to www.brightpathoutreach.org</p>
  <div class="footer-rule abs"></div>
  <nav class="footer-nav abs">Home<span>|</span>About Us<span>|</span>Menu<span>|</span>Locations<span>|</span>Kiosk Options<span>|</span>Fundraising<span>|</span>Contact Us</nav>
  <div class="copyright abs">Copyright &copy; 2013. Sun-Pod. All rights reserved</div>
  <div class="follow abs">Follow us :</div>
  <span class="social abs" style="left:863px;background:#2b62a8"></span>
  <span class="social abs" style="left:893px;background:#2f9ad6"></span>
  <span class="social abs" style="left:923px;background:#1d7a9c"></span>
  <span class="social abs" style="left:953px;background:#e9a11f"></span>
</footer>

</body>
</html>
```